Customer Waiting Area Wall Art

We're an automotive repair shop and looking to add some visually stunning artwork to our front show room/waiting area, we need to add some sound deadening panels to one of the walls and figured we'd get them custom printed with a branded mural of some kind. The wall is 12 foot wide and 8 foot tall, we were thinking of having an image of the Superstition Mountains in Arizona on there with our logo as the focal point, we had a desk at one point that was similarly designed and people liked it, though we're open to ideas for the wall too. We do not want vehicles on there as we're expanding our offerings and we don't want the artwork to create any limiting assumptions to clients. There are a couple of pictures of the wall we want to cover, we'll move the wheel rack, as well as some of the new desks and shelves currently in the waiting area, the previous desk we've retired and just a picture of the Superstitions we liked.

```html
<!DOCTYPE html>
<html lang="en">
<head>
<meta charset="UTF-8">
<title>Ironback Diesel Performance – Waiting Area Mural</title>
<link rel="stylesheet" href="https://fonts.googleapis.com/css2?family=Playfair+Display:ital@1&family=Montserrat:wght@800&family=Oswald:wght@600&display=swap">
<style>
  :root {
    --backdrop: #e9e7e9;
    --ink: #110f0d;
    --brand-red: #b02418;
    --button-red: #c0392b;
    --paper: #ffffff;
    --sky-top: #b4b3dc;
    --sky-pink: #dcb6cf;
    --rock: #a4513f;
    --rock-deep: #82412f;
    --slope: #7e8a5c;
    --scrub: #aaa68b;
    --social: #8a8a90;
  }
  * { margin: 0; padding: 0; box-sizing: border-box; }
  html, body {
    width: 1200px; height: 900px; overflow: hidden;
    background: var(--backdrop);
  }
  .mural {
    position: absolute; left: 30px; top: 70px;
    width: 1140px; height: 760px;
    overflow: hidden; background: var(--ink);
  }
  .mural__landscape {
    position: absolute; inset: 0;
    background: linear-gradient(180deg,
      var(--sky-top) 0%, var(--sky-pink) 10%, var(--rock) 26%,
      var(--rock-deep) 45%, var(--slope) 66%, var(--scrub) 82%);
  }
  .mural__swoosh { position: absolute; inset: 0; width: 100%; height: 100%; }
  .mural__tagline {
    position: absolute; left: 0; width: 100%; top: 180px;
    text-align: center;
    font-family: "Playfair Display", serif; font-style: italic;
    font-size: 46px; color: var(--paper);
  }
  .brand {
    position: absolute; left: 60px; top: 620px; width: 420px;
    text-align: center;
    font-family: "Montserrat", sans-serif; font-weight: 800;
    font-size: 46px; line-height: 1.05; color: var(--brand-red);
    text-transform: uppercase; letter-spacing: 1px;
  }
  .brand__sub { display: block; font-size: 17px; letter-spacing: 6px; margin-top: 6px; }
  .divider {
    position: absolute; left: 524px; top: 594px;
    width: 2px; height: 128px; background: var(--paper);
  }
  .divider__arrow {
    position: absolute; left: 526px; top: 645px;
    width: 0; height: 0;
    border-top: 12px solid transparent; border-bottom: 12px solid transparent;
    border-left: 20px solid var(--paper);
  }
  .social {
    position: absolute; left: 990px; top: 543px;
    display: flex; gap: 6px;
  }
  .social__dot { width: 30px; height: 30px; border-radius: 50%; background: var(--social); }
  .pitch {
    position: absolute; left: 572px; top: 592px;
    font-family: "Montserrat", sans-serif; font-weight: 800;
    font-size: 24.5px; line-height: 28px; color: var(--paper);
    text-transform: uppercase;
  }
  .web-button {
    position: absolute; left: 572px; top: 667px;
    width: 326px; height: 52px; border-radius: 4px;
    background: var(--button-red); color: var(--paper);
    font-family: "Oswald", sans-serif; font-weight: 600;
    font-size: 33px; line-height: 52px; text-align: center;
    text-transform: uppercase;
  }
  .call {
    position: absolute; left: 912px; top: 664px;
    font-family: "Montserrat", sans-serif; font-weight: 800;
    font-size: 23px; line-height: 28px; color: var(--paper);
  }
</style>
</head>
<body>
  <main class="mural">
    <div class="mural__landscape" role="img" aria-label="Photograph of the Superstition Mountains in Arizona at dusk: red rock cliffs under a pink and lavender sky, with cholla and saguaro cactus on the desert slope"></div>

    <svg class="mural__swoosh" viewBox="0 0 1738 1158" preserveAspectRatio="none" aria-hidden="true">
      <path fill="var(--ink)" d="M0,615 C500,735 1000,815 1465,822 L1738,735 L1738,1158 L0,1158 Z"/>
      <path fill="var(--ink)" d="M1150,600 C1200,580 1500,650 1738,735 L1738,830 L1465,822 Z"/>
      <path fill="var(--paper)" d="M0,640 C400,735 700,800 830,820 C600,800 300,750 0,715 Z"/>
      <path fill="var(--brand-red)" d="M0,360 C350,560 800,760 1465,815 C1000,800 500,720 0,615 Z"/>
      <path fill="var(--paper)" d="M1050,760 C1100,740 1110,620 1150,585 C1180,560 1230,545 1285,545 L1290,560 C1200,575 1140,605 1165,645 C1220,705 1400,780 1465,812 C1300,808 1150,782 1050,760 Z"/>
      <path fill="var(--brand-red)" d="M1150,600 C1130,560 1180,530 1290,530 C1450,530 1650,570 1738,605 L1738,735 C1550,670 1300,585 1200,590 C1175,593 1160,598 1150,600 Z"/>
    </svg>

    <p class="mural__tagline">This place was friendly enough</p>

    <p class="brand">Ironback<span class="brand__sub">Diesel Performance</span></p>

    <div class="divider"></div>
    <div class="divider__arrow"></div>

    <div class="social" aria-label="Social media">
      <span class="social__dot"></span>
      <span class="social__dot"></span>
      <span class="social__dot"></span>
    </div>

    <p class="pitch">Veteran owned/operated business<br>Specializing in light duty diesels</p>

    <p class="web-button">ironback-diesel.com</p>

    <p class="call">OR CALL US:<br>(480) 555-0147</p>
  </main>
</body>
</html>
```